HOME IMPROVEMENT Business Card

I want a very unique business card. nothing typical and boring. Im open to you ideas. Ive seen cards with gold and silver or color foil and spot UV coatings. Im looking for something that looks cool and grabs attention. I like rounded corners but am open to all suggestions. We are a home improvement company and I will have a presentation folder printed and a catalog printed also and want to keep that same theme. I love the colors in our logo but I am open at looking at a 3rd color that would work with my logo. I hope that helps.
Card should include
Address
Phone
Fax
Email
Website
Target Market(s)
Home owners, people looking to remodel their home
Industry/Entity Type
Home Improvement
Contact Information for Business Card
2873 Maple Crest Avenue Unit 410
Des Plaines, Il 60284
Phone
Direct Line
Email
Website
Font styles to use
Other font styles liked:
- IM OPEN MINDED
Requirements
Must have
- High end quality look nothing boring I like rounded corners but am open minded
Nice to have
- WOW. I want something nice and impressive.
Should not have
- ??? Not sure

```html
<!DOCTYPE html>
<html lang="en">
<head>
<meta charset="utf-8">
<title>Hearthline Remodeling Co. – Business Card</title>
<link rel="stylesheet" href="https://fonts.googleapis.com/css2?family=Exo+2:wght@400;500;700&display=swap">
<style>
  :root {
    --backdrop: #e8e3e0;
    --frost: #f5f2f1;
    --navy: #12133f;
    --green: #00994a;
    --white: #ffffff;
    --ghost: #c9d3ce;
  }
  * { margin: 0; padding: 0; box-sizing: border-box; }
  html, body {
    width: 1200px; height: 900px; overflow: hidden;
    background: var(--backdrop);
    font-family: "Exo 2", sans-serif;
  }
  .canvas { position: relative; width: 1200px; height: 900px; }
  .card {
    position: absolute;
    border-radius: 40px;
    overflow: hidden;
    background: var(--frost);
    box-shadow: 0 10px 30px rgba(0,0,0,0.12);
  }
  .card--front { left: 78px; top: 35px; width: 587px; height: 363px; }
  .card--back { left: 388px; top: 505px; width: 567px; height: 353px; }

  .brand-area {
    position: absolute; left: 0; top: 0; right: 0; height: 197px;
    display: flex; align-items: center; justify-content: center;
  }
  .brand-name {
    font-weight: 700; font-size: 44px; color: var(--navy);
    letter-spacing: 0.5px; padding-top: 10px;
  }
  .brand-name--ghost {
    color: var(--ghost); transform: scaleX(-1);
  }
  .card--back .brand-area { height: 195px; }

  .contact-band {
    position: absolute; left: 0; right: 0; top: 197px; bottom: 0;
    background: var(--navy);
    display: grid; grid-template-columns: 297px 1fr;
    padding: 64px 0 0 34px;
    color: var(--white); font-size: 16px; letter-spacing: 0.3px;
  }
  .contact-list { list-style: none; }
  .contact-list li {
    display: flex; align-items: center; gap: 9px; height: 27px;
  }
  .contact-icon { width: 17px; height: 17px; flex: none; }

  .address-band {
    position: absolute; left: 0; right: 0; top: 195px; bottom: 0;
    background: var(--green);
    display: flex; align-items: center; justify-content: center;
    color: var(--white); font-size: 16px; letter-spacing: 0.3px;
  }
</style>
</head>
<body>
<main class="canvas">

  <section class="card card--front" aria-label="Business card front">
    <div class="brand-area">
      <span class="brand-name">Hearthline Remodeling Co.</span>
    </div>
    <div class="contact-band">
      <ul class="contact-list">
        <li>
          <svg class="contact-icon" viewBox="0 0 17 17" aria-hidden="true">
            <rect width="17" height="17" rx="3" fill="#fff"/>
            <path d="M4 7.5c0-1.5 2-2.5 4.5-2.5S13 6 13 7.5v0.8h-2.2V7.2H6.2v1.1H4z M5.5 9h6l1 3.5h-8z" fill="#12133f"/>
          </svg>
          (044)123456789
        </li>
        <li>
          <svg class="contact-icon" viewBox="0 0 17 17" aria-hidden="true">
            <rect width="17" height="17" rx="3" fill="#fff"/>
            <path d="M4 7.5c0-1.5 2-2.5 4.5-2.5S13 6 13 7.5v0.8h-2.2V7.2H6.2v1.1H4z M5.5 9h6l1 3.5h-8z" fill="#12133f"/>
          </svg>
          (044)123456789(DIRECT)
        </li>
      </ul>
      <ul class="contact-list" style="margin-top:-3px">
        <li>
          <svg class="contact-icon" viewBox="0 0 17 17" aria-hidden="true">
            <rect width="17" height="17" rx="3" fill="#fff"/>
            <rect x="4" y="5.5" width="9" height="6.5" fill="#12133f"/>
            <path d="M4 5.5l4.5 3.5 4.5-3.5" stroke="#fff" stroke-width="1" fill="none"/>
          </svg>
          info@youremail.com
        </li>
        <li>
          <svg class="contact-icon" viewBox="0 0 17 17" aria-hidden="true">
            <rect width="17" height="17" rx="3" fill="#fff"/>
            <circle cx="8.5" cy="8.5" r="4.5" fill="none" stroke="#12133f" stroke-width="1.4"/>
            <path d="M4 8.5h9M8.5 4c-2 2.5-2 6.5 0 9M8.5 4c2 2.5 2 6.5 0 9" stroke="#12133f" stroke-width="1" fill="none"/>
          </svg>
          www.websitename.com
        </li>
      </ul>
    </div>
  </section>

  <section class="card card--back" aria-label="Business card back">
    <div class="brand-area">
      <span class="brand-name brand-name--ghost">Hearthline Remodeling Co.</span>
    </div>
    <div class="address-band">
      <p class="address">2873 Maple Crest Avenue Unit 410 Des Plaines, Il 60284</p>
    </div>
  </section>

</main>
</body>
</html>
```